Vesk Architecture

We are a architectural design and build company working between scales 1/1000 to 1/1 we want people to understand our difference from our design experience and quality.we build hotels restourants and office spaces.Our company name is Vesk architecture to mind sustainability.

We want to write our adress phone and work spesifications on the card and we want our logo as backround.

Ps:you could find the logo adress and phone box numbers from the web:www.veskmimarlik-ornek.com

Target Market(s)

Who looks for experts.

Industry/Entity Type

Architecture

Requirements
Must have
• Design is over everything.
Should not have
• we don want it to be colorfull

```html
<!DOCTYPE html>
<html lang="en">
<head>
<meta charset="utf-8">
<title>Vesk Architecture – Business Card</title>
<link rel="stylesheet" href="https://fonts.googleapis.com/css2?family=Jost:wght@300;400&display=swap">
<style>
  :root {
    --page-bg: #ffffff;
    --card-bg: #9a7a66;
    --ink-light: #f7f1ea;
  }
  * { margin: 0; padding: 0; box-sizing: border-box; }
  html, body {
    width: 1200px;
    height: 591px;
    overflow: hidden;
    background: var(--page-bg);
  }
  .canvas {
    position: relative;
    width: 1200px;
    height: 591px;
  }
  .business-card {
    position: absolute;
    left: 199px;
    top: 56px;
    width: 870px;
    height: 482px;
    background: var(--card-bg);
    border-radius: 10px;
    color: var(--ink-light);
    font-family: "Jost", "Futura", sans-serif;
  }
  .brand-name {
    position: absolute;
    left: 0;
    right: 0;
    top: 38px;
    text-align: center;
    font-weight: 300;
    font-size: 210px;
    line-height: 1;
    letter-spacing: 4px;
    color: var(--ink-light);
    padding-left: 50px;
  }
  .contact-block {
    position: absolute;
    left: 0;
    right: 0;
    top: 344px;
    text-align: center;
    font-weight: 400;
    font-size: 23px;
    line-height: 30px;
    letter-spacing: 0.8px;
  }
  .contact-block .phone-row span + span {
    margin-left: 46px;
  }
</style>
</head>
<body>
<main class="canvas">
  <section class="business-card" aria-label="Vesk Architecture business card">
    <h1 class="brand-name">vesk</h1>
    <address class="contact-block">
      <p class="street-line">Ceviz Mah. Liman Cad. Papatya Sok.</p>
      <p class="city-line">No:7 Liman Kadikoy/Istanbul</p>
      <p class="phone-row"><span class="phone">T.0216 555 01 47</span><span class="fax">F.0216 555 02 98</span></p>
      <p class="email-line">E-mail:veskmimarlik@ornekposta.com</p>
    </address>
  </section>
</main>
</body>
</html>
```